Themed design for packaging sleeve and box

1) Gable box 330w x 200d x 160h (image attached for illustration purposes)
2) Sleeve to wrap around our food trays - see image attached

See the images uploaded!!!
This should not be copied, as some are from our competitors and are subject to Copywrite but gives an idea what kind of packaging we would be creating

From all the designs submitted, we will choose one final design and work with this designer to create our full packaging range.....

Target Market(s)

Working adults and health mined people

Font styles to use
Sans Serif

Colors

Designer to choose colors to be used in the design.

Requirements
Must have
• A clean modern look, striking design
Same design in different colours (see the drink bottles idea)
1) meat in shades of red
2) fish in shades of blue
3) vegetable in shades of green
Nice to have
• abstract white against strong colours
use shapes or mosaic or shades of the same colours
Should not have
• overpacked designs with too much information

```html
<!DOCTYPE html>
<html lang="en">
<head>
<meta charset="utf-8">
<title>Evenplate Gable Box Dieline</title>
<link rel="stylesheet" href="https://fonts.googleapis.com/css2?family=Quicksand:wght@500&family=Fira+Sans+Condensed:wght@600&display=swap">
<style>
  :root {
    --brand-green: #33cc33;
    --leaf-green: #4a7a35;
    --veg-light: #f3f6f1;
    --veg-dark: #9bb58c;
    --paper: #ffffff;
    --die-line: #000000;
    --fold-line: #8a8a8a;
    --white-type: #ffffff;
  }
  html, body {
    margin: 0;
    padding: 0;
    width: 1200px;
    height: 848px;
    overflow: hidden;
    background: var(--paper);
  }
  .dieline { display: block; width: 1200px; height: 848px; }
  .colour-block { fill: var(--brand-green); }
  .cut { fill: none; stroke: var(--die-line); stroke-width: 3; stroke-linejoin: round; }
  .fold-thin { fill: none; stroke: var(--die-line); stroke-width: 1; }
  .fold-grey { fill: none; stroke: var(--fold-line); stroke-width: 1; }
  .wordmark {
    font-family: "Quicksand", sans-serif;
    font-weight: 500;
    font-size: 50px;
    text-anchor: middle;
  }
  .wordmark--white { fill: var(--white-type); }
  .wordmark--green { fill: var(--brand-green); font-size: 64px; }
  .descriptor {
    font-family: "Quicksand", sans-serif;
    font-weight: 500;
    font-size: 14px;
    letter-spacing: 13px;
    fill: var(--brand-green);
    text-anchor: middle;
  }
  .tagline {
    font-family: "Fira Sans Condensed", sans-serif;
    font-weight: 600;
    font-size: 21px;
    letter-spacing: 1px;
    fill: var(--leaf-green);
  }
</style>
</head>
<body>
<svg class="dieline" viewBox="0 0 2290 1620" preserveAspectRatio="none" xmlns="http://www.w3.org/2000/svg">
  <defs>
    <linearGradient id="veg-fade-left" x1="0" y1="0" x2="1" y2="0">
      <stop offset="0" stop-color="var(--veg-dark)"/>
      <stop offset="1" stop-color="var(--veg-light)"/>
    </linearGradient>
    <linearGradient id="veg-fade-right" x1="1" y1="0" x2="0" y2="0">
      <stop offset="0" stop-color="var(--veg-dark)"/>
      <stop offset="1" stop-color="var(--veg-light)"/>
    </linearGradient>
  </defs>

  <!-- colour blocks -->
  <g class="colour-blocks">
    <rect class="colour-block" x="117" y="276" width="382" height="1078"/>
    <rect class="colour-block" x="821" y="360" width="386" height="1015"/>
    <rect class="colour-block" x="1513" y="333" width="330" height="1013"/>
  </g>

  <!-- vegetable artwork areas -->
  <rect x="499" y="780" width="122" height="306" fill="url(#veg-fade-left)" role="img" aria-label="Green ink drawing of cauliflower, cabbage, broccoli and carrots"/>
  <rect x="1391" y="780" width="122" height="306" fill="url(#veg-fade-right)" role="img" aria-label="Green ink drawing of cauliflower, cabbage, broccoli and carrots"/>

  <!-- left side panel with handle -->
  <g class="side-panel side-panel--left">
    <path class="cut" d="M202,507 L202,405 Q202,394 214,394 L258,394 Q264,392 268,400 L274,414 L274,352 Q274,336 304,336 L727,336 Q763,336 763,365 L763,430 L772,404 Q776,394 782,394 L812,394 Q822,396 822,410 L822,507 Z"/>
    <path class="cut" d="M337,507 L337,445 Q337,421 370,421 L655,421 Q683,421 684,450 L686,507"/>
    <path class="cut" d="M236,507 L188,778 M775,507 L822,778"/>
    <path class="cut" d="M185,1087 V1328 H455 L515,1266 H656 L710,1328 L818,1329 V1090 M820,1090 L656,1266"/>
  </g>

  <!-- right side panel with handle -->
  <g class="side-panel side-panel--right">
    <path class="cut" d="M1222,507 L1222,405 Q1222,394 1234,394 L1278,394 Q1284,392 1288,400 L1294,414 L1294,352 Q1294,336 1324,336 L1747,336 Q1783,336 1783,365 L1783,430 L1792,404 Q1796,394 1802,394 L1832,394 Q1842,396 1842,410 L1842,507 Z"/>
    <path class="cut" d="M1357,507 L1357,445 Q1357,421 1390,421 L1675,421 Q1703,421 1704,450 L1706,507"/>
    <path class="cut" d="M1256,507 L1208,778 M1795,507 L1842,778"/>
    <path class="cut" d="M1210,1087 V1328 H1479 L1540,1266 H1681 L1735,1328 L1843,1329 V1090 M1845,1090 L1681,1266"/>
  </g>

  <!-- front and back gable tops -->
  <g class="gable-top">
    <path class="cut" d="M821,778 L925,407 Q926,394 945,394 L1113,394 Q1133,396 1137,410 L1207,778"/>
    <rect class="cut" x="1006" y="467" width="30" height="133" rx="15"/>
    <path class="cut" d="M1843,778 L1945,407 Q1946,394 1965,394 L2133,394 Q2153,396 2157,410 L2228,778"/>
    <rect class="cut" x="2025" y="467" width="30" height="133" rx="15"/>
  </g>

  <!-- base flaps -->
  <path class="fold-thin" d="M821,1090 L872,1265 H1030 L1207,1090"/>
  <path class="fold-grey" d="M1848,1090 L2022,1265 H2180 L2232,1090"/>

  <!-- wall band -->
  <g class="wall-band">
    <path class="fold-thin" d="M185,778 L138,792 L138,1075 L185,1087"/>
    <rect class="cut" x="185" y="778" width="2043" height="309"/>
    <path class="cut" d="M821,778 V1087 M1207,778 V1087 M1843,778 V1087"/>
  </g>

  <!-- brand and copy -->
  <text class="wordmark wordmark--white" x="337" y="946">evenplate</text>
  <text class="wordmark wordmark--white" x="1015" y="946">evenplate</text>
  <text class="wordmark wordmark--white" x="1685" y="946">evenplate</text>
  <text class="wordmark wordmark--green" x="2037" y="946">evenplate</text>
  <text class="descriptor" x="2043" y="966">KOSHER MEALS</text>

  <g class="tagline">
    <text x="640" y="915">LOREM IPSUM</text>
    <text x="640" y="948">SOLLICITIDUM</text>
    <text x="640" y="981">PELLENTESQUE</text>
    <text x="1243" y="915">LOREM IPSUM</text>
    <text x="1243" y="948">SOLLICITIDUM</text>
    <text x="1243" y="981">PELLENTESQUE</text>
  </g>
</svg>
</body>
</html>
```